Visitenkarten-Design für Boutique-Unternehmensberatung
Zielgruppe
Boutique Unternehmensberatung für die Chemische Industrie. Wir unterstützen Unternehmen, die Beziehung zu Ihren Händlern zu optimieren.
Vorläufige Website kernwerk-consult.de kann ggf weitere Einblicke geben. Hinweis: Diese Website wurde bisher noch nicht professionell erstellt.
Aufgabenstellung
Die Visitenkarte sollte vertrauenserweckend und seriös wirken. Zeitgleich aber auch modern.

```html
<!DOCTYPE html>
<html lang="de">
<head>
<meta charset="utf-8">
<title>Visitenkarte – Kernwerk Consult</title>
<link href="https://fonts.googleapis.com/css2?family=Montserrat:wght@400;500;700;800&display=swap" rel="stylesheet">
<style>
  :root {
    --brand-blue: #03427c;
    --paper: #f1f1f1;
    --backdrop: #d6d6d6;
    --ink: #2a2a2a;
    --white: #ffffff;
  }
  * { box-sizing: border-box; margin: 0; padding: 0; }
  html, body { width: 1200px; height: 1000px; overflow: hidden; }
  body {
    background: var(--backdrop);
    font-family: "Montserrat", sans-serif;
    display: flex;
    flex-direction: column;
    align-items: center;
    justify-content: center;
    gap: 60px;
  }
  .card {
    position: relative;
    width: 620px;
    height: 400px;
    box-shadow: 0 6px 18px rgba(0,0,0,0.12);
  }
  /* back side */
  .card-back {
    background: var(--brand-blue);
    color: var(--white);
    display: flex;
    flex-direction: column;
    align-items: center;
    justify-content: center;
  }
  .back-mark {
    display: flex;
    align-items: center;
    gap: 16px;
    margin-top: -20px;
  }
  .mark-dot {
    flex: none;
    width: 34px; height: 34px; border-radius: 50%;
    background: var(--paper);
  }
  .back-name {
    font-weight: 700;
    font-size: 40px;
    color: var(--paper);
    letter-spacing: 0.5px;
  }
  .back-url {
    position: absolute;
    bottom: 70px;
    font-size: 17px;
    letter-spacing: 2px;
    color: var(--paper);
  }
  /* front side */
  .card-front {
    background: var(--paper);
    color: var(--ink);
    border-bottom: 6px solid var(--brand-blue);
  }
  .front-brand {
    position: absolute;
    left: 50px; top: 150px;
    width: 200px;
    display: flex; align-items: center; gap: 12px;
  }
  .front-brand .mark-dot { width: 22px; height: 22px; background: var(--brand-blue); }
  .front-name {
    font-weight: 700; font-size: 26px; color: var(--brand-blue); line-height: 1.1;
  }
  .address {
    position: absolute;
    left: 50px; top: 265px;
    display: flex; gap: 14px; align-items: flex-end;
    font-size: 15px; line-height: 1.7;
  }
  .person {
    position: absolute;
    right: 45px; top: 55px;
    width: 255px;
  }
  .person-name {
    font-weight: 800; font-size: 24px; color: var(--brand-blue);
  }
  .person-role {
    font-size: 17px; letter-spacing: 0.5px; margin-top: 2px;
  }
  .rule {
    width: 80px; height: 3px; background: var(--brand-blue); margin: 12px 0 20px;
  }
  .contact-list { list-style: none; font-size: 15px; }
  .contact-list li {
    display: flex; justify-content: space-between; align-items: center;
    height: 30px;
  }
  .contact-list svg { flex: none; width: 16px; height: 16px; }
</style>
</head>
<body>
  <section class="card card-back">
    <div class="back-mark">
      <span class="mark-dot"></span>
      <span class="back-name">Kernwerk Consult</span>
    </div>
    <p class="back-url">www.kernwerk-consult.de</p>
  </section>

  <section class="card card-front">
    <div class="front-brand">
      <span class="mark-dot"></span>
      <span class="front-name">Kernwerk<br>Consult</span>
    </div>

    <div class="address">
      <svg width="14" height="18" viewBox="0 0 14 18" aria-hidden="true">
        <path d="M7 0a7 7 0 0 0-7 7c0 5 7 11 7 11s7-6 7-11a7 7 0 0 0-7-7z" fill="var(--brand-blue)"/>
        <circle cx="7" cy="7" r="2.6" fill="var(--paper)"/>
      </svg>
      <p>Lindenallee 12<br>28195 Bremen</p>
    </div>

    <div class="person">
      <h1 class="person-name">Lena Hartmann</h1>
      <p class="person-role">HR MANAGER</p>
      <div class="rule"></div>
      <ul class="contact-list">
        <li><span>0421 - 55810 00</span>
          <svg viewBox="0 0 16 16" aria-label="Telefon"><path d="M3 1l3 3-1.5 2a9 9 0 0 0 5.5 5.5L12 10l3 3-2 2C7 15 1 9 1 3z" fill="var(--brand-blue)"/></svg>
        </li>
        <li><span>0421 - 55810 99</span>
          <svg viewBox="0 0 16 16" aria-label="Fax"><rect x="4" y="1" width="8" height="4" fill="var(--brand-blue)"/><rect x="1" y="6" width="14" height="6" rx="1" fill="var(--brand-blue)"/><rect x="4" y="10" width="8" height="5" fill="var(--paper)" stroke="var(--brand-blue)" stroke-width="1.2"/></svg>
        </li>
        <li><span>info@kernwerk-consult.de</span>
          <svg viewBox="0 0 16 16" aria-label="Web"><circle cx="8" cy="8" r="7" fill="none" stroke="var(--brand-blue)" stroke-width="1.5"/><ellipse cx="8" cy="8" rx="3" ry="7" fill="none" stroke="var(--brand-blue)" stroke-width="1.2"/><line x1="1" y1="8" x2="15" y2="8" stroke="var(--brand-blue)" stroke-width="1.2"/></svg>
        </li>
      </ul>
    </div>
  </section>
</body>
</html>
```